Game, Voice & Dedicated Server Company Needs a Business Card Design

We need a new business card design, centered around our new logo (PSD provided below).

Designs that we do like:
https://pixelmarsh.net/item/corporate-business-card/5382017?s_rank=43 (needs to be made more eye catching)

Our main areas of business are:
- Dedicated Servers
- Game Servers
- Voice Servers
- Mitigation Security Specialists

Industry/Entity Type

Business

Contact Information for Business Card

On the card: (and anything else you would suggest)
- Staff member name
- Staff member position in company
- Staff member phone number
- Staff member email
- Other / Staff member Skype
- Website link

Colors
9bcb3c
abd036

Requirements
Must have
• Design of Card:
• - Green (same green as the logo)
• - Business / Corporate design
• - Something a little different / abstract that shouts premium

```html
<!DOCTYPE html>
<html lang="en">
<head>
<meta charset="utf-8">
<title>Brightlane Hosting – Business Card</title>
<link href="https://fonts.googleapis.com/css2?family=Arimo:wght@400;700&display=swap" rel="stylesheet">
<style>
  :root {
    --green: #8dc63f;
    --green-dark: #7ab32e;
    --ink: #4d4d4f;
    --charcoal: #1b1b1b;
    --charcoal-light: #3a3a3a;
    --stage: #4a4a4a;
    --white: #ffffff;
  }
  * { margin: 0; padding: 0; box-sizing: border-box; }
  html, body { width: 999px; height: 1200px; overflow: hidden; }
  body {
    background: radial-gradient(ellipse at 50% 40%, #555 0%, var(--stage) 55%, #333 100%);
    font-family: "Arimo", Arial, sans-serif;
    position: relative;
  }
  .card {
    position: absolute;
    left: 31px;
    width: 937px;
    height: 536px;
    overflow: hidden;
  }
  .card--front { top: 70px; background: var(--white); }
  .card--back {
    top: 625px;
    background: radial-gradient(ellipse at 50% 30%, var(--charcoal-light) 0%, #262626 50%, var(--charcoal) 100%);
  }

  /* front */
  .front-base { position: absolute; left: 0; top: 440px; }
  .brand {
    position: absolute;
    display: flex;
    align-items: center;
  }
  .brand__mark { background: var(--green); flex: none; }
  .brand__name {
    color: var(--green);
    font-weight: 700;
    line-height: 0.95;
    letter-spacing: -0.5px;
    text-transform: uppercase;
  }
  .brand--front { left: 42px; top: 226px; gap: 18px; }
  .brand--front .brand__mark { width: 72px; height: 72px; }
  .brand--front .brand__name { font-size: 37px; }

  .contact { position: absolute; left: 546px; top: 84px; }
  .contact__name {
    color: var(--green);
    font-weight: 700;
    font-size: 30px;
    line-height: 1;
  }
  .contact__role {
    color: var(--ink);
    font-size: 22px;
    margin-top: 15px;
  }
  .contact__list { list-style: none; margin-top: 44px; }
  .contact__item {
    display: flex;
    align-items: center;
    height: 38px;
    margin-bottom: 14px;
    color: var(--ink);
    font-size: 24px;
  }
  .contact__icon {
    width: 38px; height: 38px;
    background: var(--green);
    display: flex; align-items: center; justify-content: center;
    margin-right: 17px;
    flex: none;
  }

  /* back */
  .brand--back { left: 156px; top: 188px; gap: 26px; }
  .brand--back .brand__mark { width: 110px; height: 110px; }
  .brand--back .brand__name { font-size: 62px; }
  .back-band {
    position: absolute;
    left: 0; top: 437px;
    width: 100%; height: 44px;
    background: var(--green);
    display: flex; align-items: center; justify-content: center;
    color: var(--charcoal);
    font-size: 22px;
    letter-spacing: 3.6px;
  }
</style>
</head>
<body>

<section class="card card--front">
  <svg class="front-base" width="937" height="96" viewBox="0 0 937 96" aria-hidden="true">
    <rect x="0" y="0" width="937" height="96" fill="#ffffff"/>
    <path d="M0 35 H480 C520 35 528 10 575 10 H937 V96 H0 Z" fill="var(--green)"/>
    <path d="M0 58 H470 C515 58 525 10 575 10 H937 V96 H0 Z" fill="var(--charcoal)"/>
  </svg>

  <div class="brand brand--front">
    <span class="brand__mark"></span>
    <span class="brand__name">Brightlane<br>Hosting</span>
  </div>

  <div class="contact">
    <p class="contact__name">Name Surname</p>
    <p class="contact__role">CEO &amp; Managing Director</p>
    <ul class="contact__list">
      <li class="contact__item">
        <span class="contact__icon">
          <svg width="20" height="20" viewBox="0 0 24 24" aria-hidden="true"><path fill="#fff" d="M6.6 10.8a15 15 0 0 0 6.6 6.6l2.2-2.2a1 1 0 0 1 1-.25 11.4 11.4 0 0 0 3.6.57 1 1 0 0 1 1 1V20a1 1 0 0 1-1 1A17 17 0 0 1 3 4a1 1 0 0 1 1-1h3.5a1 1 0 0 1 1 1c0 1.25.2 2.45.57 3.57a1 1 0 0 1-.25 1z"/></svg>
        </span>00 0000 0000
      </li>
      <li class="contact__item">
        <span class="contact__icon">
          <svg width="16" height="20" viewBox="0 0 16 20" aria-hidden="true"><rect x="2" y="1" width="12" height="18" rx="2" fill="none" stroke="#fff" stroke-width="2"/><circle cx="8" cy="15.5" r="1.2" fill="#fff"/></svg>
        </span>0000 000 000
      </li>
      <li class="contact__item">
        <span class="contact__icon">
          <svg width="22" height="18" viewBox="0 0 22 18" aria-hidden="true"><rect x="1" y="2" width="20" height="14" fill="#fff"/><path d="M1 2 L11 10 L21 2" fill="none" stroke="var(--green)" stroke-width="1.6"/></svg>
        </span>info@brightlane.com.au
      </li>
      <li class="contact__item">
        <span class="contact__icon">
          <svg width="22" height="22" viewBox="0 0 22 22" aria-hidden="true" fill="none" stroke="#fff" stroke-width="1.5"><circle cx="11" cy="11" r="9"/><ellipse cx="11" cy="11" rx="4" ry="9"/><path d="M2 11h18M3.5 6.5h15M3.5 15.5h15"/></svg>
        </span>www.brightlane.com.au
      </li>
    </ul>
  </div>
</section>

<section class="card card--back">
  <div class="brand brand--back">
    <span class="brand__mark"></span>
    <span class="brand__name">Brightlane<br>Hosting</span>
  </div>
  <div class="back-band">www.brightlane.com.au</div>
</section>

</body>
</html>
```